Private Mortgage Bank needs a brochure designed.

We need a brochure designed for a new Private Mortgage Bank based in Maryland. We provide financing options for real estate investors who are purchasing or refinancing an investment property. Our website is v4harborlend (dot) com. We are rental property specialists. I will attach our current logo and the business card design we have.
Real Estate Investors
Finance

```html
<!DOCTYPE html>
<html lang="en">
<head>
<meta charset="utf-8">
<title>Harbor Lend – Rental Property Specialists Flyer</title>
<link rel="stylesheet" href="https://fonts.googleapis.com/css2?family=Oranienbaum&family=Open+Sans:wght@400;600;700&family=Dancing+Script:wght@500&display=swap">
<style>
  :root {
    --green: #3f6a2c;
    --green-dark: #35591f;
    --green-light: #7f9a70;
    --ink: #6a6a6a;
    --ink-strong: #555555;
    --paper: #ffffff;
    --backdrop: #e4e4e4;
    --suit: #1c2230;
  }
  * { box-sizing: border-box; margin: 0; padding: 0; }
  html, body { width: 1200px; height: 800px; overflow: hidden; background: var(--backdrop); }
  .flyer {
    position: absolute; left: 299px; top: 11px;
    width: 602px; height: 778px;
    background: var(--paper); overflow: hidden;
    font-family: "Open Sans", sans-serif;
  }
  .hero-photo {
    position: absolute; left: 0; top: 0; width: 602px; height: 410px;
    background: linear-gradient(180deg, var(--suit) 0%, #2e3646 30%, #8a8f98 52%, #e9e9e9 75%, #ffffff 100%);
  }
  .header-shapes { position: absolute; left: 0; top: 0; }
  .brand {
    position: absolute; left: 20px; top: 140px; width: 180px;
    display: flex; align-items: center; justify-content: center; gap: 8px;
    color: var(--paper); font-weight: 600; font-size: 18px; letter-spacing: 1px;
    white-space: nowrap;
  }
  .brand-mark { width: 12px; height: 12px; background: var(--paper); flex: none; }
  .headline {
    position: absolute; left: 26px; top: 398px;
    font-family: "Oranienbaum", serif; font-weight: 400; color: var(--green);
    font-size: 98px; line-height: 81px; white-space: nowrap;
    transform: scaleX(0.6); transform-origin: left top;
  }
  .about {
    position: absolute; left: 284px; top: 418px; width: 294px;
    color: var(--ink); font-size: 11.4px; line-height: 15.5px;
  }
  .about p + p { margin-top: 15px; }
  .about strong { color: var(--ink-strong); font-weight: 700; font-size: 14px; }
  .tagline {
    position: absolute; left: 0; width: 602px; top: 664px; text-align: center;
    font-family: "Dancing Script", cursive; color: var(--green);
    font-size: 30px; white-space: nowrap;
  }
  .footer { position: absolute; left: 0; top: 718px; }
  .website {
    position: absolute; left: 18px; top: 743px;
    color: var(--paper); font-size: 18px; letter-spacing: 1px; white-space: nowrap;
  }
  .phone {
    position: absolute; right: 44px; top: 741px;
    color: var(--green); font-size: 21px; font-weight: 700; letter-spacing: 0.5px; white-space: nowrap;
  }
</style>
</head>
<body>
  <main class="flyer">
    <div class="hero-photo" role="img" aria-label="Photo of a hand stacking coins beside a small model house with a red roof on a desk with charts and banknotes"></div>

    <svg class="header-shapes" width="602" height="300" viewBox="0 0 602 300" aria-hidden="true">
      <path d="M0 0 H414 L320 235 Q306 262 276 264 H0 Z" fill="var(--green)"/>
      <path d="M414 0 H428 L334 236 Q318 276 276 276 H0 V264 H276 Q306 262 320 235 Z" fill="var(--paper)"/>
      <path d="M385 0 H602 V126 Z" fill="var(--green)"/>
      <path d="M385 0 H440 L520 32 Z" fill="var(--green-light)" opacity="0.8"/>
    </svg>

    <div class="brand"><span class="brand-mark"></span>HARBOR LEND</div>

    <h1 class="headline">Rental<br>Property<br>Specialists</h1>

    <section class="about">
      <p><strong>Harbor Lend, LLC</strong> is a private mortgage bank exclusively focusing on financing rental properties.</p>
      <p>We finance these transactions using our capital; all underwriting is done in-house. We have $100 million to lend, with our minimum loan amount being $150,000 and our maximum loan amount at $3 million.</p>
      <p>Our asset classes consist of Residential 1-4 unit properties, including SFR, Townhome, Modular, Condominium, Duplex, Triplex, and Fourplex, and Multi-Family 5-8 unit properties. Grow your net worth through the strategic creation of a rental property portfolio.</p>
    </section>

    <p class="tagline">Earn Through Incremental Income &amp; Appreciation</p>

    <svg class="footer" width="602" height="60" viewBox="0 0 602 60" aria-hidden="true">
      <path d="M0 8 H300 Q330 8 350 30 L380 60 H0 Z" fill="var(--green)"/>
    </svg>
    <p class="website">www.v4harborlend.com</p>
    <p class="phone">+1 (410) 555-0187</p>
  </main>
</body>
</html>
```